Equity, Effectiveness and Efficiency in charitable food relief sector

I am undertaking my PhD in food policy in the charitable food relief sector, specifically investigating the factors (supply, demand and capacity) that affect the introduction of nutrition policy and in turn, affect the sector's ability to achieve equity, effectiveness and efficiency.

I need a graphic device that incorporates this central idea of Equity, Effectiveness and Efficiency, and how the factors of supply, demand and capacity interact. There are sub-factors within supply (1-6), demand (7-10) and capacity (11 - 15). All these details are shown in the attached figure (Basic figure_Eq Effec Effic and factors.jpg)

This figure (Basic figure_Eq Effec Effic and factors.jpg) contains all the information I need in a graphic but I need something that is more visually appealing, and that can link the ideas in a format other than a table. The final graphic will outline how the food relief sector balances the core objectives of equity, effectiveness and efficiency with the factors (and sub-factors) of supply, demand and capacity.

```html
<!DOCTYPE html>
<html lang="en">
<head>
<meta charset="utf-8">
<title>Equity, Effectiveness, Efficiency – Factors in Charitable Food Relief</title>
<link rel="stylesheet" href="https://fonts.googleapis.com/css2?family=Outfit:wght@300;400;500;700;800&display=swap">
<style>
  :root {
    --supply-green: #69b84a;
    --demand-orange: #eb9430;
    --capability-blue: #1274bd;
    --title-navy: #1e2266;
    --ring-grey: #e6e6e8;
    --white: #ffffff;
  }
  html, body {
    margin: 0;
    padding: 0;
    width: 1200px;
    height: 927px;
    overflow: hidden;
    background: var(--white);
    font-family: "Outfit", Arial, sans-serif;
  }
  .figure {
    position: relative;
    width: 1200px;
    height: 927px;
  }
  .wheel {
    position: absolute;
    left: 0;
    top: 0;
  }
  .core-title {
    position: absolute;
    left: 0;
    width: 1200px;
    top: 22px;
    margin: 0;
    text-align: center;
    color: var(--title-navy);
    font-weight: 800;
    font-size: 42px;
    line-height: 45px;
    letter-spacing: 0.5px;
  }
  .factor-heading {
    position: absolute;
    margin: 0;
    color: var(--white);
    font-weight: 700;
    font-size: 51px;
    line-height: 1;
    letter-spacing: 1px;
  }
  .factor-heading--supply { left: 63px; top: 148px; }
  .factor-heading--demand { left: 0; width: 1192px; text-align: center; top: 412px; }
  .factor-heading--capability { left: 872px; top: 148px; }

  .factor-list {
    position: absolute;
    margin: 0;
    padding: 0;
    list-style: none;
    color: var(--white);
    font-size: 21px;
  }
  .factor-list li {
    position: relative;
    white-space: nowrap;
  }
  .factor-list .tick {
    position: absolute;
    width: 18px;
    height: 14px;
    top: 50%;
    margin-top: -8px;
  }
  .factor-list--supply { left: 69px; top: 202px; }
  .factor-list--supply li { height: 46px; line-height: 46px; padding-left: 31px; font-weight: 500; }
  .factor-list--supply .tick { left: 0; }

  .factor-list--demand { left: 464px; top: 488px; }
  .factor-list--demand li { height: 46px; line-height: 46px; padding-left: 31px; font-weight: 500; }
  .factor-list--demand .tick { left: 0; }

  .factor-list--capability { left: 877px; top: 210px; }
  .factor-list--capability li { line-height: 30px; height: 30px; }
  .factor-list--capability .main-factor { padding-left: 35px; font-weight: 500; }
  .factor-list--capability .main-factor + .main-factor,
  .factor-list--capability .sub-factor + .main-factor { margin-top: 13px; }
  .factor-list--capability .main-factor .tick { left: 0; }
  .factor-list--capability .sub-factor { padding-left: 35px; font-weight: 300; }
  .sub-factor .arrow { display: inline-block; width: 20px; font-size: 17px; }

  .factor-icon { position: absolute; }
  .factor-icon--supply { left: 66px; top: 48px; }
  .factor-icon--demand { left: 546px; top: 312px; }
  .factor-icon--capability { left: 872px; top: 46px; }
</style>
</head>
<body>
<main class="figure">
  <svg class="wheel" width="1200" height="927" viewBox="0 0 1200 927" aria-hidden="true">
    <defs>
      <clipPath id="wheel-clip">
        <circle cx="600" cy="0" r="805"/>
      </clipPath>
      <radialGradient id="core-fill" cx="600" cy="0" r="210" gradientUnits="userSpaceOnUse">
        <stop offset="0.6" stop-color="#ffffff"/>
        <stop offset="1" stop-color="#f1f1f2"/>
      </radialGradient>
      <path id="ring-path" d="M 359 33.8 A 243 243 0 0 0 841 33.8"/>
    </defs>
    <g clip-path="url(#wheel-clip)">
      <rect class="segment-supply" x="0" y="0" width="1200" height="927" fill="var(--supply-green)"/>
      <polygon class="segment-demand" points="600,0 493,247 280,739 240,830 600,927 960,830 919,739 707,247" fill="var(--demand-orange)"/>
      <polygon class="segment-capability" points="600,0 707,247 919,739 960,830 1200,927 1200,0" fill="var(--capability-blue)"/>
    </g>
    <circle class="core-ring" cx="600" cy="0" r="268" fill="var(--ring-grey)"/>
    <circle class="core-centre" cx="600" cy="0" r="210" fill="url(#core-fill)"/>
    <text class="ring-caption" font-family="Outfit, Arial, sans-serif" font-size="18" font-weight="400" fill="var(--title-navy)" letter-spacing="1.6">
      <textPath href="#ring-path" startOffset="50%" text-anchor="middle">FACTORS AFFECTING THE INTRODUCTION OF NUTRITION POLICY</textPath>
    </text>
  </svg>

  <h1 class="core-title">EQUITY,<br>EFFECTIVENESS,<br>EFFICIENCY</h1>

  <!-- Supply -->
  <svg class="factor-icon factor-icon--supply" width="98" height="92" viewBox="0 0 98 92" aria-hidden="true">
    <g fill="none" stroke="var(--white)" stroke-width="4" stroke-linejoin="round">
      <polygon points="3,22 62,22 62,82 3,82"/>
      <polygon points="3,22 22,3 82,3 62,22"/>
      <polygon points="62,22 82,3 82,62 62,82"/>
      <polyline points="23,22 42,3"/>
      <polyline points="42,22 61,3"/>
    </g>
    <polygon points="23,22 42,22 42,52 37,47 32,52 28,47 23,52" fill="var(--white)"/>
    <circle cx="72" cy="70" r="18" fill="var(--supply-green)" stroke="var(--white)" stroke-width="4"/>
    <path d="M72 60 V79 M64 71 L72 79 L80 71" fill="none" stroke="var(--white)" stroke-width="3.5" stroke-linecap="round" stroke-linejoin="round"/>
  </svg>
  <h2 class="factor-heading factor-heading--supply">SUPPLY</h2>
  <ul class="factor-list factor-list--supply">
    <li><svg class="tick" viewBox="0 0 18 14"><path d="M2 7 L7 12 L16 2" fill="none" stroke="#fff" stroke-width="2.6" stroke-linecap="round" stroke-linejoin="round"/></svg>Uncertain material supply</li>
    <li><svg class="tick" viewBox="0 0 18 14"><path d="M2 7 L7 12 L16 2" fill="none" stroke="#fff" stroke-width="2.6" stroke-linecap="round" stroke-linejoin="round"/></svg>Uncertain monetary supply</li>
    <li><svg class="tick" viewBox="0 0 18 14"><path d="M2 7 L7 12 L16 2" fill="none" stroke="#fff" stroke-width="2.6" stroke-linecap="round" stroke-linejoin="round"/></svg>Limited food supply</li>
    <li><svg class="tick" viewBox="0 0 18 14"><path d="M2 7 L7 12 L16 2" fill="none" stroke="#fff" stroke-width="2.6" stroke-linecap="round" stroke-linejoin="round"/></svg>Perishability</li>
    <li><svg class="tick" viewBox="0 0 18 14"><path d="M2 7 L7 12 L16 2" fill="none" stroke="#fff" stroke-width="2.6" stroke-linecap="round" stroke-linejoin="round"/></svg>Donor constraints</li>
    <li><svg class="tick" viewBox="0 0 18 14"><path d="M2 7 L7 12 L16 2" fill="none" stroke="#fff" stroke-width="2.6" stroke-linecap="round" stroke-linejoin="round"/></svg>Donor relationships</li>
  </ul>

  <!-- Demand -->
  <svg class="factor-icon factor-icon--demand" width="98" height="92" viewBox="0 0 98 92" aria-hidden="true">
    <g fill="none" stroke="var(--white)" stroke-width="4" stroke-linejoin="round">
      <polygon points="3,22 62,22 62,82 3,82"/>
      <polygon points="3,22 22,3 82,3 62,22"/>
      <polygon points="62,22 82,3 82,62 62,82"/>
      <polyline points="23,22 42,3"/>
      <polyline points="42,22 61,3"/>
    </g>
    <polygon points="23,22 42,22 42,52 37,47 32,52 28,47 23,52" fill="var(--white)"/>
    <circle cx="72" cy="70" r="18" fill="var(--demand-orange)" stroke="var(--white)" stroke-width="4"/>
    <path d="M72 80 V61 M64 69 L72 61 L80 69" fill="none" stroke="var(--white)" stroke-width="3.5" stroke-linecap="round" stroke-linejoin="round"/>
  </svg>
  <h2 class="factor-heading factor-heading--demand">DEMAND</h2>
  <ul class="factor-list factor-list--demand">
    <li><svg class="tick" viewBox="0 0 18 14"><path d="M2 7 L7 12 L16 2" fill="none" stroke="#fff" stroke-width="2.6" stroke-linecap="round" stroke-linejoin="round"/></svg>Uncertain demand</li>
    <li><svg class="tick" viewBox="0 0 18 14"><path d="M2 7 L7 12 L16 2" fill="none" stroke="#fff" stroke-width="2.6" stroke-linecap="round" stroke-linejoin="round"/></svg>Limited demand visibility</li>
    <li><svg class="tick" viewBox="0 0 18 14"><path d="M2 7 L7 12 L16 2" fill="none" stroke="#fff" stroke-width="2.6" stroke-linecap="round" stroke-linejoin="round"/></svg>Client choice</li>
    <li><svg class="tick" viewBox="0 0 18 14"><path d="M2 7 L7 12 L16 2" fill="none" stroke="#fff" stroke-width="2.6" stroke-linecap="round" stroke-linejoin="round"/></svg>Food wastage</li>
  </ul>

  <!-- Capability -->
  <svg class="factor-icon factor-icon--capability" width="114" height="90" viewBox="0 0 114 90" aria-hidden="true">
    <g fill="none" stroke="var(--white)">
      <circle cx="38" cy="50" r="28" stroke-width="9" stroke-dasharray="9 7.6"/>
      <circle cx="38" cy="50" r="24" stroke-width="4"/>
      <circle cx="38" cy="50" r="12" stroke-width="4"/>
      <circle cx="92" cy="20" r="15" stroke-width="6" stroke-dasharray="5.2 4.2"/>
      <circle cx="92" cy="20" r="12.5" stroke-width="3"/>
      <circle cx="92" cy="20" r="6" stroke-width="3"/>
    </g>
  </svg>
  <h2 class="factor-heading factor-heading--capability">CAPABILITY</h2>
  <ul class="factor-list factor-list--capability">
    <li class="main-factor"><svg class="tick" viewBox="0 0 18 14"><path d="M2 7 L7 12 L16 2" fill="none" stroke="#fff" stroke-width="2.6" stroke-linecap="round" stroke-linejoin="round"/></svg>Storage</li>
    <li class="sub-factor"><span class="arrow">→</span>Cold</li>
    <li class="sub-factor"><span class="arrow">→</span>Warehouse</li>
    <li class="main-factor"><svg class="tick" viewBox="0 0 18 14"><path d="M2 7 L7 12 L16 2" fill="none" stroke="#fff" stroke-width="2.6" stroke-linecap="round" stroke-linejoin="round"/></svg>Transportation</li>
    <li class="main-factor"><svg class="tick" viewBox="0 0 18 14"><path d="M2 7 L7 12 L16 2" fill="none" stroke="#fff" stroke-width="2.6" stroke-linecap="round" stroke-linejoin="round"/></svg>Workspace</li>
    <li class="sub-factor"><span class="arrow">→</span> Volunteers</li>
    <li class="sub-factor"><span class="arrow">→</span> Expertise and training</li>
    <li class="sub-factor"><span class="arrow">→</span> Attitudes and Beliefs</li>
    <li class="sub-factor"><span class="arrow">→</span>Collaboration</li>
    <li class="sub-factor"><span class="arrow">→</span>Executive Support</li>
    <li class="main-factor"><svg class="tick" viewBox="0 0 18 14"><path d="M2 7 L7 12 L16 2" fill="none" stroke="#fff" stroke-width="2.6" stroke-linecap="round" stroke-linejoin="round"/></svg>External stakeholders</li>
    <li class="main-factor"><svg class="tick" viewBox="0 0 18 14"><path d="M2 7 L7 12 L16 2" fill="none" stroke="#fff" stroke-width="2.6" stroke-linecap="round" stroke-linejoin="round"/></svg>Budget</li>
  </ul>
</main>
</body>
</html>
```